Brochure Design Project - Brelwick Motors Auto Repair Centre

We require a high quality brochure (A3 folded to A4) for us to send to local businesses to try and get more sales. We would like to keep our current colour scheme from our flyers. We are garagemark approved so we require this logo to be included in the design. The font used on our flyer is QuickLinesRG available from fontvault-example.com
This is a brief of the information we require on our brochure (the feedback from our current customers still to be received but it will be limited to 1 line each) :
Introduction to Brelwick Motors
Based in Cumbernauld, Brelwick Motors are a family run Auto service centre and believe in giving helpful, friendly expert advice in plain English. We have a wealth of experience in a wide range of vehicles and we invest heavily in equipment to ensure our work is completed to the highest possible quality standards.
It is our aim to deliver a quality service at competitive rates for our customers. We have just expanded by investing in a new 4000 sq/ft workshop to help support our ever expanding customer base.
Why are we the best choice for your business?
Choosing a garage for your business can be a tough decision. Who do you choose and who do you trust? Cost will of course be high on your list, so why take your car to a main dealer and pay main dealer prices?
• Brelwick Motors Cumbernauld can carry out servicing and repairs to main dealer standards without the high prices. We can also maintain your vehicles warranty by using genuine manufacturer's parts.
• Communication is key – we never leave you wondering when your vehicle is going to be returned. 98% of vehicles we maintain are returned the same day.
• We never carry out any work to a vehicle without prior agreement – so no unexpected bills. You always get a fully itemised VAT invoice.
• We can arrange payment terms that are suitable to both businesses.
• We have flexibility with our working hours to ensure your fleet stays on the road no matter how big or small.
• We also pride ourselves on providing a professional and efficient service, your vehicle will be looked after as if it was our own pride and joy.
How can we guarantee quality?
Garage mark is the Trading Standards code of practice for garages. We are the only independent garage in Cumbernauld to achieve this standard. We are audited to ensure we comply with the code at all times and we must follow a strict complaints procedure should the need arise.
All parts fitted are covered by a 3 month or 6000 mile warranty. *Does not include wear and tear
What services can we offer your business?
MOT Testing
Vehicle Servicing
Budget & Performance Tyres
Mechanical Repairs
Exhausts, DPF filters & CAT’s
Brake repair specialist
Same day Clutch repairs
Gearboxes
Starter motors
Alternators
Wheel Alignment
MOT Welding
Replacement Batteries
ECU Fault Diagnostics & Service resets
Collection and drop off services
We are comprehensively insured to drive all of our customers’ vehicles so we can collect vehicles at a time that suits you and deliver them back with minimal impact to your business. The only time we will ever drive your vehicles is during transportation or testing.
Our current business customers – testimonials
Pettigrew Roofing
Crest Fitting
Hollowbys
Ruvan Loader training
Sample price list
£74.17 for car service/small vans
£91.67 for commercials up to 3500kgs (class IV)
Mot’s £35 for cars and vans (class IV)
Tyre sample prices – Vantor Swift £36.95, Kelda Carro £32.45, Vantor Haulier £41.55.
Labour rate of £35.00ph
All prices exclude VAT at applicable rate, unless stated otherwise and are correct at time of printing. Subject to change without prior notice. No VAT on MOT's
Contact Us
Brelwick Motors can be contacted to discuss your individual requirement by -
Phone: 01236 482915
Email: sales@brelwick-example.co.uk
Mon – Fri 8.00am – 5.30pm
Sat – 8.00am – 4.00pm
Target Market(s)
local businesses
Industry/Entity Type
Garage
Requirements
Must have
- garagemark logo
brelwick motors logo

```html
<!DOCTYPE html>
<html lang="en">
<head>
<meta charset="utf-8">
<title>Brelwick Motors – Business Brochure</title>
<link href="https://fonts.googleapis.com/css2?family=Michroma&family=Source+Sans+3:wght@400;600;700&display=swap" rel="stylesheet">
<style>
  :root {
    --sky-top: #78b4ee;
    --sky-bottom: #80e9f3;
    --icon-blue: #5b9be6;
    --heading-yellow: #f4f23a;
    --heading-edge: #c9b81a;
    --ink: #111a24;
    --white: #ffffff;
    --badge-teal: #1f8aa8;
  }
  * { box-sizing: border-box; margin: 0; padding: 0; }
  html, body { width: 1200px; height: 849px; overflow: hidden; }
  body {
    font-family: "Source Sans 3", "Myriad Pro", sans-serif;
    color: var(--ink);
  }
  .brochure {
    position: relative;
    width: 1200px;
    height: 849px;
    background: linear-gradient(180deg, var(--sky-top) 0%, #7cc8f1 50%, var(--sky-bottom) 100%);
    overflow: hidden;
  }
  .illustration {
    position: absolute;
    background: var(--icon-blue);
    opacity: .85;
  }
  .gears { left: 500px; top: 16px; width: 180px; height: 140px; border-radius: 50%; }
  .battery { left: 528px; top: 195px; width: 148px; height: 105px; border-radius: 8px; }
  .engine { left: 520px; top: 370px; width: 158px; height: 110px; border-radius: 14px; }
  .filter { left: 560px; top: 518px; width: 80px; height: 170px; border-radius: 10px; }
  .tyre { left: 1040px; top: 690px; width: 200px; height: 200px; border-radius: 50%; }

  .block { position: absolute; }
  .heading {
    font-family: "Michroma", "Arial Black", sans-serif;
    color: var(--heading-yellow);
    text-transform: uppercase;
    line-height: 1.1;
    letter-spacing: .3px;
    white-space: nowrap;
    -webkit-text-stroke: .4px var(--heading-edge);
  }

  .intro { left: 46px; top: 42px; width: 470px; font-size: 15.5px; line-height: 21px; }
  .intro p + p { margin-top: 11px; }

  .why { left: 46px; top: 243px; width: 520px; }
  .why .heading { font-size: 19.5px; }
  .why .lead { font-size: 16.5px; font-weight: 700; line-height: 21px; margin-top: 17px; width: 460px; }
  .why .lead + .lead { margin-top: 9px; }
  .benefits { list-style: none; margin-top: 14px; font-size: 12.5px; line-height: 16px; width: 500px; }
  .benefits li { position: relative; padding-left: 24px; margin-bottom: 7px; }
  .benefits li::before { content: "☆"; position: absolute; left: 0; top: 0; font-size: 12px; }

  .quality { left: 46px; top: 680px; width: 500px; }
  .quality .heading { font-size: 16px; }
  .quality p { font-size: 11.5px; line-height: 20.5px; white-space: nowrap; }
  .quality .heading + p { margin-top: 6px; }
  .approval-badge {
    position: absolute; left: 485px; top: 766px; width: 64px; height: 66px;
    background: var(--badge-teal);
  }

  .collection { left: 700px; top: 42px; width: 470px; }
  .collection .heading { font-size: 18px; }
  .collection p { font-size: 10.5px; line-height: 17.5px; margin-top: 6px; width: 460px; }

  .testimonials { left: 700px; top: 170px; width: 450px; }
  .testimonials .heading { font-size: 18px; }
  .testimonial { font-size: 10.5px; line-height: 15px; margin-top: 10px; }
  .testimonials .heading + .testimonial { margin-top: 12px; }
  .testimonial .client { color: var(--white); font-weight: 700; font-size: 13px; }

  .prices { left: 700px; top: 464px; width: 480px; }
  .prices .heading { font-size: 25px; }
  .price-line { font-size: 20.5px; font-weight: 600; line-height: 24px; margin-top: 15px; }
  .price-line strong { font-weight: 700; }
  .prices .heading + .price-line { margin-top: 18px; }
  .tyre-prices { display: flex; margin-top: 12px; font-size: 20.5px; font-weight: 600; line-height: 30px; }
  .tyre-prices > span { width: 199px; flex: none; }
  .tyre-prices ul { list-style: none; }
  .labour { margin-top: 18px; }
</style>
</head>
<body>
<main class="brochure">
  <div class="illustration gears" role="img" aria-label="Pair of interlocking gears"></div>
  <div class="illustration battery" role="img" aria-label="Car battery with lightning bolt"></div>
  <div class="illustration engine" role="img" aria-label="Car engine block"></div>
  <div class="illustration filter" role="img" aria-label="Fuel filter"></div>
  <div class="illustration tyre" role="img" aria-label="Car wheel and tyre"></div>

  <section class="block intro">
    <p>Based in Cumbernauld, Brelwick Motors are a family run Auto service centre and believe in giving helpful, friendly expert advice in plain English. We have a wealth of experience in a wide range of vehicles and we invest heavily in equipment to ensure our work is completed to the highest possible quality standards.</p>
    <p>It is our aim to deliver a quality service at competitive rates for our customers. We have just expanded by investing in a new 4000 sq/ft workshop to help support our ever expanding customer base.</p>
  </section>

  <section class="block why">
    <h2 class="heading">Why are we the best choice<br>for your business?</h2>
    <p class="lead">Choosing a garage for your business can be a tough decision.</p>
    <p class="lead">Who do you choose and who do you trust?</p>
    <p class="lead">Cost will of course be high on your list, so why take your car to a main dealer and pay main dealer prices?</p>
    <ul class="benefits">
      <li>Brelwick Motors Cumbernauld can carry out servicing and repairs to main dealer standards without the high prices. We can also maintain your vehicles warranty by using genuine manufacturer’s parts.</li>
      <li>Communication is key – we never leave you wondering when your vehicle is going to be returned. 98% of vehicles we maintain are returned the same day.</li>
      <li>We never carry out any work to a vehicle without prior agreement – so no unexpected bills. You always get a fully itemised VAT invoice.</li>
      <li>We can arrange payment terms that are suitable to both businesses.</li>
      <li>We have flexibility with our working hours to ensure your fleet stays on the road no matter how big or small.</li>
      <li>We also pride ourselves on providing a professional and efficient service, your vehicle will be looked after as if it was our own pride and joy.</li>
    </ul>
  </section>

  <section class="block quality">
    <h2 class="heading">How can we guarantee quality?</h2>
    <p>Garage mark is the Trading Standards code of practice for garages.<br>
    We are the only independent garage in Cumbernauld to achieve this standard.<br>
    We are audited to ensure we comply with the code at all times and we must follow a strict<br>
    complaints procedure should the need arise.<br>
    All parts fitted are covered by a 3 month or 6000 mile warranty.<br>
    *Does not include wear and tear</p>
  </section>
  <div class="approval-badge" role="img" aria-label="Code of practice approval badge"></div>

  <section class="block collection">
    <h2 class="heading">Collection and drop off<br>services</h2>
    <p>We are comprehensively insured to drive all of our customers’ vehicles so we can collect vehicles at a time that suits you and deliver them back with minimal impact to your business. The only time we will ever drive your vehicles is during transportation or testing.</p>
  </section>

  <section class="block testimonials">
    <h2 class="heading">Our current business<br>customers – testimonials</h2>
    <p class="testimonial"><span class="client">Pettigrew Roofing</span> – quote quote quote quote quote quote quote quote quote quote quote quote quote quote quote quote quote quote quote quote quote quote quote quote</p>
    <p class="testimonial"><span class="client">Crest Fitting</span> – quote quote quote quote quote quote quote quote quote quote quote quote quote quote quote quote quote quote quote quote quote quote quote quote quote quote quote quote quote quote quote quote quote quote quote quote</p>
    <p class="testimonial"><span class="client">Hollowbys</span> – quote quote quote quote quote quote quote quote quote quote quote quote quote quote quote quote quote quote quote quote quote quote quote quote quote quote quote quote quote quote quote quote quote quote quote quote</p>
    <p class="testimonial"><span class="client">Ruvan Loader training</span> – quote quote quote quote quote quote quote quote quote quote quote quote quote quote quote quote quote quote quote quote quote quote quote quote quote quote quote quote quote quote quote quote quote</p>
  </section>

  <section class="block prices">
    <h2 class="heading">Sample price list</h2>
    <p class="price-line"><strong>£74.17</strong> for car service/small vans</p>
    <p class="price-line"><strong>£91.67</strong> for commercials up to 3500kgs (Class IV)</p>
    <p class="price-line">MOT’s <strong>£35</strong> for cars and vans (Class IV)</p>
    <div class="tyre-prices">
      <span>Tyre sample prices –</span>
      <ul>
        <li>Vantor Swift <strong>£36.95</strong></li>
        <li>Kelda Carro <strong>£32.45</strong></li>
        <li>Vantor Haulier <strong>£41.55</strong></li>
      </ul>
    </div>
    <p class="price-line labour">Labour rate of <strong>£35.00ph</strong></p>
  </section>
</main>
</body>
</html>
```